First Aid Training business needs business card design

We would like a double sided business card designed for a first aid training business - Banksia First Aid. We provide first aid training and , WHS (work, health and safety) training.

The attached word document contains the key information we would like on each side of the business card.

Final design needs to be delivered in print ready format, along with the original file.

```html
<!DOCTYPE html>
<html lang="en">
<head>
<meta charset="utf-8">
<title>Banksia First Aid – Business Card</title>
<link href="https://fonts.googleapis.com/css2?family=Josefin+Sans:wght@300;400;700&family=Montserrat:wght@700&display=swap" rel="stylesheet">
<style>
  :root {
    --bg: #cacaca;
    --card: #ffffff;
    --red: #f5141c;
    --ink: #111111;
    --grey-band: #6f7a7a;
    --rule: #555555;
    --text: #1c1c1c;
  }
  * { margin: 0; padding: 0; box-sizing: border-box; }
  html, body { width: 1200px; height: 846px; overflow: hidden; }
  body { background: var(--bg); position: relative; font-family: "Josefin Sans", sans-serif; color: var(--text); }

  .card {
    position: absolute;
    width: 508px; height: 290px;
    background: var(--card);
    border: 1px solid #222;
    overflow: hidden;
  }
  .card--front { left: 344px; top: 114px; }
  .card--back  { left: 345px; top: 445px; }

  /* Front */
  .brand-mark {
    position: absolute; left: 92px; top: 57px;
    width: 90px; height: 90px; border-radius: 50%;
    background: var(--red);
  }
  .brand-name {
    position: absolute; left: 44px; top: 160px; width: 186px;
    font-family: "Montserrat", sans-serif; font-weight: 700;
    font-size: 24px; line-height: 28px; color: var(--ink);
    text-align: center; letter-spacing: 0.5px;
  }
  .divider {
    position: absolute; left: 234px; top: 165px;
    width: 1px; height: 53px; background: var(--rule);
  }
  .person-name {
    position: absolute; left: 253px; top: 102px;
    font-family: "Montserrat", sans-serif; font-weight: 700;
    font-size: 22px; letter-spacing: 0.5px; color: var(--ink);
  }
  .person-name .surname { color: var(--red); }
  .contact-list { position: absolute; left: 253px; top: 158px; list-style: none; }
  .contact-list li {
    display: flex; align-items: center; height: 20.5px;
    font-size: 15px; font-weight: 300; color: var(--text);
  }
  .contact-list svg { width: 16px; height: 16px; margin-right: 6px; flex: none; }

  .band { position: absolute; left: 0; width: 100%; }
  .band--grey  { top: 253px; height: 6px; background: var(--grey-band); }
  .band--black { top: 259px; height: 7px; background: var(--ink); }
  .band--red   { top: 266px; height: 24px; background: var(--red); }

  /* Back */
  .mascot-area {
    position: absolute; left: 0; top: 0; width: 345px; height: 100%;
    background: linear-gradient(100deg, #e23a44 0%, #f04c55 45%, #f4d6d8 80%, #ffffff 100%);
  }
  .tagline { position: absolute; right: 22px; top: 62px; text-align: right; }
  .tagline__title { font-size: 27px; font-weight: 700; color: var(--red); line-height: 30px; }
  .tagline__sub { font-size: 18px; font-weight: 700; color: var(--ink); line-height: 24px; }
  .benefits { position: absolute; right: 22px; top: 144px; list-style: none; text-align: right; }
  .benefits li { font-size: 15px; font-weight: 300; line-height: 22px; }
  .benefits .dot { color: var(--red); font-weight: 700; margin-left: 8px; }
  .benefits .cont { padding-right: 12px; line-height: 16px; }
  .services {
    position: absolute; right: 22px; top: 248px;
    font-size: 15px; font-weight: 300;
  }
</style>
</head>
<body>

<section class="card card--front" aria-label="Business card front">
  <div class="brand-mark"></div>
  <div class="brand-name">BANKSIA<br>FIRST AID</div>
  <div class="divider"></div>

  <h1 class="person-name">DANIEL <span class="surname">HARTLEY</span></h1>
  <ul class="contact-list">
    <li>
      <svg viewBox="0 0 16 16" aria-hidden="true"><path d="M4 1.5l2.2 3-1.4 1.6c.8 1.8 2.3 3.4 4.1 4.3l1.5-1.4 3 2.1-1.3 2.3C7.5 13.3 2.7 8.6 1.8 3L4 1.5z" fill="var(--red)"/></svg>
      0491 570 156
    </li>
    <li>
      <svg viewBox="0 0 16 16" aria-hidden="true"><rect x="1" y="3.5" width="14" height="9" fill="var(--red)"/><path d="M1 3.5l7 5 7-5M1 12.5l5-4.5M15 12.5l-5-4.5" stroke="#fff" stroke-width="1" fill="none"/></svg>
      help@banksiafirstaid.com.au
    </li>
    <li>
      <svg viewBox="0 0 16 16" aria-hidden="true"><g fill="none" stroke="var(--red)" stroke-width="1.2"><circle cx="8" cy="8" r="6.5"/><ellipse cx="8" cy="8" rx="3" ry="6.5"/><path d="M1.5 8h13M2.5 4.8h11M2.5 11.2h11M8 1.5v13"/></g></svg>
      www.banksiafirstaid.com.au
    </li>
  </ul>

  <div class="band band--grey"></div>
  <div class="band band--black"></div>
  <div class="band band--red"></div>
</section>

<section class="card card--back" aria-label="Business card back">
  <div class="mascot-area" role="img" aria-label="Illustration of a red first aid robot mascot walking and carrying a first aid kit"></div>

  <div class="tagline">
    <p class="tagline__title">Onsite Training</p>
    <p class="tagline__sub">- We can come to you</p>
  </div>

  <ul class="benefits">
    <li>Time efficient<span class="dot">•</span></li>
    <li>Cost effective<span class="dot">•</span></li>
    <li>Minimise downtime<span class="dot">•</span></li>
    <li class="cont">for your team</li>
  </ul>

  <p class="services">First Aid Training &amp; WHS Training</p>
</section>

</body>
</html>
```